8' x 22' Enclosed work trailer

I just purchased a new work trailer and want a badass design for the exterior. Either a wrap, lettering or combo to match my truck. I have a kitchen & bathroom remodeling company - Renovo Crafters. I think it should include my logo and possibly a larger photo of a sweet kitchen and bathroom just like my old trailer. I'm attaching pics of my old trailer for reference, my existing truck, my new trailer and logo. Excited to see the results!

```html
<!DOCTYPE html>
<html lang="en">
<head>
<meta charset="utf-8">
<title>Renovo Crafters – Trailer Side Wrap</title>
<link rel="stylesheet" href="https://fonts.googleapis.com/css2?family=Montserrat:wght@700&family=Kaushan+Script&family=Saira:wght@600&display=swap">
<style>
  :root {
    --backdrop: #4a525b;
    --panel-white: #ffffff;
    --brand-blue: #1f7bc4;
    --brand-blue-light: #3f9ad9;
    --kitchen-light: #e6eaee;
    --kitchen-mid: #a9b0b8;
    --kitchen-floor: #d9c6a3;
    --bath-light: #e8dfd2;
    --bath-warm: #bfae98;
    --bath-wood: #5b3b28;
  }
  html, body {
    margin: 0;
    padding: 0;
    width: 1200px;
    height: 1193px;
    overflow: hidden;
    background: var(--backdrop);
  }
  .canvas {
    width: 1200px;
    height: 1193px;
    display: flex;
    align-items: center;
    justify-content: center;
  }
  .trailer-wrap {
    width: 1120px;
    height: 406px;
    display: block;
  }
  .brand-name {
    font-family: "Montserrat", sans-serif;
    font-weight: 700;
    fill: var(--brand-blue);
  }
  .tagline {
    font-family: "Kaushan Script", cursive;
    fill: var(--brand-blue);
  }
  .phone-number {
    font-family: "Saira", sans-serif;
    font-weight: 600;
    fill: var(--panel-white);
  }
  .web-address {
    font-family: "Montserrat", sans-serif;
    font-weight: 700;
    fill: var(--brand-blue);
  }
</style>
</head>
<body>
<main class="canvas">
  <svg class="trailer-wrap" viewBox="0 0 1675 607" xmlns="http://www.w3.org/2000/svg">
    <defs>
      <linearGradient id="kitchenTone" x1="0" y1="0" x2="0" y2="1">
        <stop offset="0" stop-color="var(--kitchen-light)"/>
        <stop offset="0.45" stop-color="var(--kitchen-mid)"/>
        <stop offset="0.75" stop-color="#8e959d"/>
        <stop offset="1" stop-color="var(--kitchen-floor)"/>
      </linearGradient>
      <linearGradient id="bathTone" x1="0" y1="0" x2="1" y2="0">
        <stop offset="0" stop-color="var(--bath-light)"/>
        <stop offset="0.55" stop-color="var(--bath-warm)"/>
        <stop offset="0.75" stop-color="var(--bath-wood)"/>
        <stop offset="1" stop-color="#d8cfc2"/>
      </linearGradient>
    </defs>

    <rect class="kitchen-photo" x="0" y="0" width="700" height="607" fill="url(#kitchenTone)"
          role="img" aria-label="Photo of a modern grey kitchen with island and wood floor"/>
    <polygon class="bathroom-photo" points="1060,0 1675,0 1675,607 1220,607" fill="url(#bathTone)"
             role="img" aria-label="Photo of a modern bathroom with freestanding tub and glass shower"/>

    <polygon class="white-panel" points="378,0 1077,0 1232,607 540,607" fill="var(--panel-white)"/>

    <polygon class="accent-stripe" points="262,0 330,0 540,607 497,607" fill="var(--brand-blue)"/>
    <polygon class="accent-stripe accent-stripe--soft" points="352,50 410,50 444,495 372,495" fill="var(--brand-blue-light)" opacity="0.75"/>
    <polygon class="accent-stripe accent-stripe--soft" points="1075,0 1117,0 1215,390 1180,390" fill="var(--brand-blue-light)" opacity="0.8"/>
    <polygon class="accent-stripe" points="1092,380 1137,380 1232,607 1172,607" fill="var(--brand-blue)"/>

    <text class="brand-name" x="785" y="225" text-anchor="middle" font-size="66" textLength="590" lengthAdjust="spacingAndGlyphs">Renovo Crafters</text>
    <text class="tagline" x="782" y="320" text-anchor="middle" font-size="40" textLength="570" lengthAdjust="spacingAndGlyphs">“Unsurpassed Quality &amp; Design”</text>

    <polygon class="phone-bar" points="572,385 1090,385 1078,448 560,448" fill="var(--brand-blue)"/>
    <text class="phone-number" x="827" y="437" text-anchor="middle" font-size="62" textLength="490" lengthAdjust="spacingAndGlyphs">555-301-48000</text>

    <text class="web-address" x="826" y="485" text-anchor="middle" font-size="24" textLength="368" lengthAdjust="spacingAndGlyphs">www.renovo-crafters.com</text>
  </svg>
</main>
</body>
</html>
```